Business Card Design Project 4 Construction Business

I am after a creative, but sleek and simple/ clean business card design. This design will form the basis of future items and might include a logo or simply a creative way to lay out the text of my company name 'kestrel ventures'
I like the simplicity of black and white however I would also be happy to see a splash of colour introduced somehow to give the text some interest and make it stand out.
I would like a double sided card.
I am young (ish!) and professional, offering construction and project management services, what I don't want is the traditional builders type card featuring a cheesy hammer/ saw image etc.
As the company name, kestrel ventures, suggests, we focus on working closely and collaboratively together, in synergy with all stakeholders involved in the projects that we undertake
Construction

```html
<!DOCTYPE html>
<html lang="en">
<head>
<meta charset="utf-8">
<title>Kestrel Ventures – Business Card</title>
<link rel="stylesheet" href="https://fonts.googleapis.com/css2?family=Michroma&family=Arimo:wght@400&display=swap">
<style>
  :root {
    --ink: #0b0b0b;
    --paper: #ffffff;
    --tile-light: #efefef;
    --tile-mid: #d6d6d6;
  }
  * { margin: 0; padding: 0; box-sizing: border-box; }
  html, body { width: 1200px; height: 741px; overflow: hidden; background: var(--paper); }
  .card {
    position: relative;
    width: 1200px;
    height: 741px;
    background: var(--paper);
    color: var(--ink);
    font-family: "Arimo", Arial, sans-serif;
  }
  .brand {
    position: absolute;
    left: 56px;
    top: 40px;
    font-family: "Michroma", sans-serif;
    font-weight: 400;
    color: var(--ink);
    text-transform: uppercase;
  }
  .brand-main {
    display: block;
    font-size: 50px;
    line-height: 60px;
    letter-spacing: 6px;
  }
  .brand-sub {
    display: block;
    font-size: 27px;
    line-height: 44px;
    letter-spacing: 27px;
    margin-left: 6px;
  }
  .name-bar {
    position: absolute;
    left: 0;
    top: 249px;
    width: 315px;
    height: 42px;
    background: var(--ink);
  }
  .person {
    position: absolute;
    left: 56px;
    top: 246px;
    font-family: "Michroma", sans-serif;
    font-size: 34px;
    line-height: 48px;
    letter-spacing: 2px;
    text-transform: uppercase;
    white-space: nowrap;
  }
  .person-first {
    color: var(--paper);
    display: inline-block;
    width: 280px;
  }
  .person-last { color: var(--ink); }
  .role {
    position: absolute;
    left: 56px;
    top: 294px;
    font-size: 31px;
    letter-spacing: 3px;
  }
  .tile-art {
    position: absolute;
    left: 766px;
    top: 68px;
    width: 365px;
    height: 376px;
    border-radius: 8px;
    background: radial-gradient(circle at 45% 55%, var(--tile-mid) 0%, var(--tile-light) 55%, var(--paper) 100%);
  }
  .contact-band {
    position: absolute;
    left: 0;
    top: 516px;
    width: 1200px;
    height: 225px;
    background: var(--ink);
    color: var(--paper);
  }
  .website {
    position: absolute;
    right: 37px;
    top: 8px;
    font-size: 19px;
    letter-spacing: 1.5px;
  }
  .contact-list { list-style: none; position: absolute; left: 58px; top: 36px; }
  .contact-item {
    display: flex;
    align-items: center;
    height: 52px;
    letter-spacing: 2px;
  }
  .contact-item svg { width: 30px; height: 26px; margin-right: 12px; flex: none; }
  .contact-phone { font-size: 31px; }
  .contact-email, .contact-address { font-size: 25px; }
</style>
</head>
<body>
<div class="card">
  <div class="brand">
    <span class="brand-main">Kestrel</span>
    <span class="brand-sub">Ventures</span>
  </div>

  <div class="name-bar"></div>
  <div class="person"><span class="person-first">Liam</span><span class="person-last">Corbett</span></div>
  <div class="role">Director</div>

  <div class="tile-art" role="img" aria-label="Cluster of overlapping translucent grey squares"></div>

  <div class="contact-band">
    <div class="website">www.kestrelventuresgroup.com.au</div>
    <ul class="contact-list">
      <li class="contact-item contact-phone">
        <svg viewBox="0 0 30 26" aria-hidden="true"><path fill="#fff" d="M2 8c0-4 6-6 13-6s13 2 13 6v3h-7V8c-2-1-10-1-12 0v3H2z"/><path fill="#fff" d="M7 12h16l4 6v6H3v-6z"/><circle cx="15" cy="18" r="3" fill="#0b0b0b"/></svg>
        0400 555 019
      </li>
      <li class="contact-item contact-email">
        <svg viewBox="0 0 30 26" aria-hidden="true"><rect x="3" y="5" width="24" height="16" fill="none" stroke="#fff" stroke-width="1.5"/><path d="M3 5l12 9 12-9M3 21l9-8M27 21l-9-8" fill="none" stroke="#fff" stroke-width="1.5"/></svg>
        liam@kestrelventuresgroup.com.au
      </li>
      <li class="contact-item contact-address">
        <svg viewBox="0 0 30 26" aria-hidden="true"><path d="M3 13L15 3l12 10M7 11v11h16V11" fill="none" stroke="#fff" stroke-width="2.5"/></svg>
        14 Harbour Ln Northbridge NSW 2063
      </li>
    </ul>
  </div>
</div>
</body>
</html>
```